Job site for plomvarinex.com

Update: Looking for a really simple design that is fit for a short attention span.
Need a website built that I can host on Brimfoxa.com.
Need tracking: Important to track where students are clicking and be able to provide that detail to employers.
The site will use the plomvarinex.com logo (attached).
Add a tagline - Highschool Students Start Here
( Link on main page) Job Opportunities (click to page)
- Listing of new jobs.
o Job Title
o Company Name
o Position Description
o Hyperlink to employer website (need to be able to track clicks)
(Link on main page) Tools & Career Advice (click to page)
o This section would allow for the posting of advice and articles.
(Link on main page) Ask a Job Question? (click to page)
o Submit a question via email – email only collected. No personal
info.
(Link on main page) Volunteer Opportunities (click to page)
o A listing of organizations that need student volunteers. Need
to be able to add a new listing. Similar to a job listing:
Business or Non-profit Name
Description of need
Hyperlink to website or simply contact info.
(Link on main page) About Us
- Be able to change the content
Updates
Target Market(s)
Ages 14-18
Industry/Entity Type
job board
Coding
Coded - Design and coding required
Number of Pages Required
4 page
Look and feel

```html
<!DOCTYPE html>
<html lang="en">
<head>
<meta charset="utf-8">
<title>plomvarinex.com — Website and App Design</title>
<link rel="stylesheet" href="https://fonts.googleapis.com/css2?family=Montserrat:wght@500;700;800&family=Open+Sans:wght@400;600;700&display=swap">
<style>
:root{
  --bg-top:#22b4ea;
  --bg-bottom:#1b6fc2;
  --cyan:#3fc3ee;
  --cyan-soft:#d6f1fb;
  --dark:#3b4550;
  --ink:#2c3a48;
  --muted:#8a97a3;
  --line:#d3dbe2;
  --white:#ffffff;
  --red:#d8283c;
  --navy:#2c5fa8;
}
*{box-sizing:border-box;margin:0;padding:0}
html,body{width:1200px;height:2596px;overflow:hidden}
body{
  position:relative;
  background:linear-gradient(160deg,var(--bg-top) 0%,var(--bg-bottom) 100%);
  font-family:"Open Sans",Arial,sans-serif;color:var(--ink);
}
.section-title{
  position:absolute;left:0;width:1200px;text-align:center;
  font-family:"Montserrat",Arial,sans-serif;font-weight:800;
  font-size:58px;letter-spacing:1px;color:var(--white);
}
.section-title.web{top:82px}
.section-title.app{top:1240px}

/* ---------- website pages ---------- */
.page{
  position:absolute;top:272px;width:248px;height:668px;
  background:var(--white);overflow:hidden;
  box-shadow:0 6px 18px rgba(0,40,90,.25);
}
.page.p1{left:32px}.page.p2{left:328px}.page.p3{left:624px}.page.p4{left:920px}

.topbar{height:14px;background:var(--white);border-bottom:2px solid var(--cyan);position:relative}
.topbar::after{content:"";position:absolute;right:12px;top:4px;width:60px;height:5px;border-radius:3px;background:var(--cyan)}

.brand{display:flex;align-items:center;justify-content:center;gap:6px}
.brand .dot{width:22px;height:22px;border-radius:50%;background:var(--dark)}
.brand .name{font-family:"Montserrat",Arial,sans-serif;font-weight:700;font-size:15px;color:var(--navy)}
.brand.center{flex-direction:column;gap:4px}
.brand.center .dot{width:40px;height:40px}

.field{height:10px;border-radius:2px;background:var(--cyan-soft);margin:0 18px 8px}
.field-label{font-size:7px;color:var(--muted);margin:0 18px 3px}

.band{background:var(--cyan);color:var(--white);text-align:center;font-family:"Montserrat",Arial,sans-serif}
.hero-band{padding:22px 14px;margin-top:14px}
.hero-band .small{font-size:9px;font-weight:500;letter-spacing:.5px}
.hero-band .big{font-size:22px;font-weight:800;line-height:1.05;margin-top:4px}

.help{text-align:center;font-family:"Montserrat",Arial,sans-serif;margin-top:22px}
.help .q{font-size:9px;font-weight:700;color:var(--ink)}
.help .a{font-size:7px;color:var(--muted);margin-top:3px}

.blob-row{display:flex;justify-content:center;gap:18px;margin-top:22px}
.blob{width:50px;height:44px;border-radius:14px;background:var(--dark)}
.tile{display:flex;flex-direction:column;align-items:center;gap:6px}
.tile .tag{width:38px;height:7px;border-radius:4px;background:var(--cyan)}
.tile .lbl{font-size:7px;color:var(--muted)}

.footer{
  position:absolute;left:0;bottom:0;width:100%;height:72px;background:var(--cyan);
  display:flex;align-items:center;justify-content:space-between;padding:0 12px;
}
.footer .name{font-family:"Montserrat",Arial,sans-serif;font-weight:700;font-size:10px;color:var(--white)}
.footer .icons{display:flex;gap:6px}
.footer .icons span{width:12px;height:12px;border-radius:3px;background:var(--white)}
.footer .bar{position:absolute;right:12px;top:12px;width:80px;height:6px;border-radius:3px;background:var(--white)}

.pills{display:flex;gap:5px;justify-content:center;margin:18px 8px 0}
.pill{font-size:7px;padding:3px 6px;border-radius:8px;background:var(--cyan-soft);color:var(--ink);font-weight:600}
.page-heading{font-family:"Montserrat",Arial,sans-serif;font-weight:800;font-size:15px;text-align:center;margin:26px 0 10px;color:var(--ink)}

.job{display:flex;align-items:center;gap:10px;margin:16px 16px 0}
.job.flip{flex-direction:row-reverse}
.job .blob{width:58px;height:44px}
.job .info{flex:1}
.job .title{font-size:8px;font-weight:700;color:var(--ink);margin-bottom:4px}
.job .ln{height:4px;background:var(--line);border-radius:2px;margin-bottom:3px}

.dots{display:flex;gap:6px;justify-content:center;margin-top:22px}
.dots span{width:7px;height:7px;border-radius:50%;background:var(--line)}
.dots span.on{background:var(--cyan)}

.copy{font-size:6px;line-height:1.45;color:var(--muted);text-align:justify}
.p3 .copy{margin:14px 18px 0;height:210px;overflow:hidden}
.team{padding:16px 10px 18px;margin-top:18px}
.team h3{font-size:15px;font-weight:800;margin-bottom:12px}
.team .people{display:flex;justify-content:space-around}
.team .person{display:flex;flex-direction:column;align-items:center;gap:4px;font-size:7px}
.team .face{width:48px;height:48px;border-radius:50%;background:var(--white)}
.contact{text-align:center;margin-top:22px}
.contact h3{font-family:"Montserrat",Arial,sans-serif;font-weight:800;font-size:15px;color:var(--ink)}
.contact .btn{width:44px;height:10px;border-radius:5px;background:var(--cyan);margin:10px auto 0}

.community-head{font-family:"Montserrat",Arial,sans-serif;font-size:12px;font-weight:700;margin:18px 0 0 16px;color:var(--ink)}
.user{display:flex;align-items:center;gap:10px;margin:20px 16px 0}
.avatar{width:26px;height:26px;border-radius:50%;background:var(--dark)}
.user .uname{font-size:8px;font-weight:700}
.video{margin:10px 16px 0;height:130px;background:var(--dark);display:flex;align-items:center;justify-content:center}
.post{margin:10px 16px 0;background:var(--dark);padding:10px}
.post .copy{color:#e6ecf1}

/* ---------- app screens ---------- */
.screen{
  position:absolute;width:212px;height:400px;background:var(--white);
  border-radius:18px;overflow:hidden;box-shadow:0 6px 18px rgba(0,40,90,.25);
}
.s1{left:214px;top:1428px}.s2{left:494px;top:1428px}.s3{left:774px;top:1428px}
.s4{left:214px;top:1928px}.s5{left:494px;top:1928px}.s6{left:774px;top:1928px}

.app-head{height:34px;display:flex;align-items:center;justify-content:space-between;padding:0 12px;border-bottom:2px solid var(--cyan)}
.app-head .name{font-family:"Montserrat",Arial,sans-serif;font-weight:700;font-size:10px;color:var(--navy)}
.menu{display:flex;flex-direction:column;gap:2px}
.menu span{width:12px;height:2px;background:var(--ink)}

.s1 .brand{margin-top:96px}
.cta{display:block;width:140px;margin:34px auto 0;padding:9px 0;border-radius:16px;background:var(--cyan);color:var(--white);text-align:center;font-family:"Montserrat",Arial,sans-serif;font-weight:700;font-size:9px}
.s1 .login{position:absolute;bottom:22px;width:100%;text-align:center;font-size:8px;color:var(--muted)}

.s2 .brand{margin-top:30px}
.s2 .form{margin-top:40px}
.s2 .field{margin:0 22px 10px}
.s2 .field-label{margin:0 22px 3px}
.app-btn{width:140px;margin:0 auto 8px;padding:5px 0;border-radius:4px;color:var(--white);text-align:center;font-size:8px;font-weight:600}
.app-btn.blue{background:var(--navy);margin-top:42px}
.app-btn.red{background:var(--red)}

.circle-row{display:flex;justify-content:center;gap:16px;margin-top:80px}
.circle-row .tile .blob{width:42px;height:42px;border-radius:50%}
.lines{margin:30px 24px 0}
.lines .ln{height:4px;background:var(--line);border-radius:2px;margin-bottom:5px}

.s4 .pills{margin-top:14px}
.s4 .page-heading{font-size:13px;margin:20px 0 6px}
.s4 .job{margin:14px 14px 0}
.s4 .job .blob{width:50px;height:38px}

.s5 .brand{margin-top:26px}
.s5 .copy{margin:16px 20px 0;height:240px;overflow:hidden}

.s6 .user{margin:16px 14px 0}
.s6 .video{margin:8px 14px 0;height:90px}
</style>
</head>
<body>

<h1 class="section-title web">WEBSITE DESIGN</h1>

<!-- Home page -->
<section class="page p1" aria-label="Home page">
  <div class="topbar"></div>
  <div class="brand center" style="margin-top:16px"><span class="dot"></span><span class="name">plomvarinex</span></div>
  <div style="margin-top:16px">
    <div class="field-label">Job title</div><div class="field"></div>
    <div class="field-label">Location</div><div class="field"></div>
    <div class="field"></div>
  </div>
  <div class="band hero-band">
    <div class="small">LOOKING FOR THE</div>
    <div class="big">BIGGEST<br>COMPANIES</div>
  </div>
  <div class="help">
    <div class="q">WHAT ARE YOU LOOKING FOR?</div>
    <div class="a">WE ARE HERE TO HELP</div>
  </div>
  <div class="blob-row">
    <div class="tile"><div class="blob"></div><div class="tag"></div><div class="lbl">Jobs</div></div>
    <div class="tile"><div class="blob"></div><div class="tag"></div><div class="lbl">Advice</div></div>
    <div class="tile"><div class="blob"></div><div class="tag"></div><div class="lbl">Volunteer</div></div>
  </div>
  <footer class="footer"><span class="bar"></span><span class="name">plomvarinex</span><span class="icons"><span></span><span></span><span></span></span></footer>
</section>

<!-- Job listings page -->
<section class="page p2" aria-label="Job listings page">
  <div class="topbar"></div>
  <nav class="pills"><span class="pill">Jobs</span><span class="pill">Advice</span><span class="pill">Questions</span><span class="pill">Volunteer</span></nav>
  <h2 class="page-heading">WAITER JOBS</h2>
  <div class="job"><div class="blob"></div><div class="info"><div class="title">JOB TITLE</div><div class="ln"></div><div class="ln" style="width:70%"></div></div></div>
  <div class="job flip"><div class="blob"></div><div class="info"><div class="title">JOB TITLE</div><div class="ln"></div><div class="ln" style="width:70%"></div></div></div>
  <div class="job"><div class="blob"></div><div class="info"><div class="title">JOB TITLE</div><div class="ln"></div><div class="ln" style="width:70%"></div></div></div>
  <div class="job flip"><div class="blob"></div><div class="info"><div class="title">JOB TITLE</div><div class="ln"></div><div class="ln" style="width:70%"></div></div></div>
  <div class="dots"><span></span><span></span><span></span><span></span><span class="on"></span></div>
  <footer class="footer"><span class="bar"></span><span class="name">plomvarinex</span><span class="icons"><span></span><span></span><span></span></span></footer>
</section>

<!-- About page -->
<section class="page p3" aria-label="About page">
  <div class="topbar"></div>
  <div class="brand center" style="margin-top:14px"><span class="dot"></span><span class="name">plomvarinex</span></div>
  <p class="copy">We help high school students find their first job. Browse new openings from local employers, read simple career advice, ask a job question by email and discover volunteer work near you. Every listing links straight to the employer so you can apply fast. Start here, build skills, earn experience and grow your future with people who want to help you succeed. New jobs are added every week for students aged fourteen to eighteen.</p>
  <div class="band team">
    <h3>OUR TEAM</h3>
    <div class="people">
      <div class="person"><div class="face" role="img" aria-label="Team member portrait"></div>Name</div>
      <div class="person"><div class="face" role="img" aria-label="Team member portrait"></div>Name</div>
      <div class="person"><div class="face" role="img" aria-label="Team member portrait"></div>Name</div>
    </div>
  </div>
  <div class="contact"><h3>CONTACT US</h3><div class="btn"></div></div>
  <footer class="footer"><span class="bar"></span><span class="name">plomvarinex</span><span class="icons"><span></span><span></span><span></span></span></footer>
</section>

<!-- Community page -->
<section class="page p4" aria-label="Community page">
  <div class="topbar"></div>
  <h2 class="community-head">community</h2>
  <div class="user"><span class="avatar"></span><span class="uname">USER NAME</span></div>
  <div class="video" role="img" aria-label="Video post">
    <svg width="34" height="38" viewBox="0 0 34 38"><path d="M2 2 L32 19 L2 36 Z" fill="#ffffff"/></svg>
  </div>
  <div class="user"><span class="avatar"></span><span class="uname">USER NAME</span></div>
  <div class="post"><p class="copy">Great tips on writing a first resume today. Remember to list school clubs, sports and any volunteer hours. Employers love reliable students who show up on time and ask good questions.</p></div>
  <footer class="footer"><span class="bar"></span><span class="name">plomvarinex</span><span class="icons"><span></span><span></span><span></span></span></footer>
</section>

<h1 class="section-title app">APP DESIGN</h1>

<!-- Welcome screen -->
<section class="screen s1" aria-label="Welcome screen">
  <div class="brand center"><span class="dot"></span><span class="name">plomvarinex</span></div>
  <span class="cta">START YOUR CAREER</span>
  <div class="login">Login | Sign up</div>
</section>

<!-- Sign in screen -->
<section class="screen s2" aria-label="Sign in screen">
  <div class="brand center"><span class="dot"></span><span class="name">plomvarinex</span></div>
  <div class="form">
    <div class="field-label">Email</div><div class="field"></div>
    <div class="field-label">Password</div><div class="field"></div>
  </div>
  <div class="app-btn blue">Sign in</div>
  <div class="app-btn red">Register</div>
</section>

<!-- Menu screen -->
<section class="screen s3" aria-label="Menu screen">
  <header class="app-head"><span class="name">plomvarinex</span><span class="menu"><span></span><span></span><span></span></span></header>
  <div class="circle-row">
    <div class="tile"><div class="blob"></div><div class="lbl">Jobs</div></div>
    <div class="tile"><div class="blob"></div><div class="lbl">Advice</div></div>
    <div class="tile"><div class="blob"></div><div class="lbl">Volunteer</div></div>
  </div>
  <div class="lines"><div class="ln"></div><div class="ln" style="width:80%"></div><div class="ln" style="width:60%"></div></div>
</section>

<!-- Job list screen -->
<section class="screen s4" aria-label="Job list screen">
  <header class="app-head"><span class="name">plomvarinex</span><span class="menu"><span></span><span></span><span></span></span></header>
  <nav class="pills"><span class="pill">Jobs</span><span class="pill">Advice</span><span class="pill">Ask</span></nav>
  <h2 class="page-heading">WAITER JOBS</h2>
  <div class="job"><div class="blob"></div><div class="info"><div class="title">JOB TITLE</div><div class="ln"></div><div class="ln" style="width:70%"></div></div></div>
  <div class="job flip"><div class="blob"></div><div class="info"><div class="title">JOB TITLE</div><div class="ln"></div><div class="ln" style="width:70%"></div></div></div>
  <div class="dots"><span></span><span></span><span></span><span class="on"></span></div>
</section>

<!-- About screen -->
<section class="screen s5" aria-label="About screen">
  <header class="app-head"><span class="name">plomvarinex</span><span class="menu"><span></span><span></span><span></span></span></header>
  <div class="brand center"><span class="dot"></span><span class="name">plomvarinex</span></div>
  <p class="copy">We connect high school students with local employers and volunteer groups. Find a job, read helpful career advice and ask questions by email. Every listing links to the employer website so applying is quick and simple. Start here and build your future one step at a time with us.</p>
</section>

<!-- Community screen -->
<section class="screen s6" aria-label="Community screen">
  <header class="app-head"><span class="name">plomvarinex</span><span class="menu"><span></span><span></span><span></span></span></header>
  <div class="user"><span class="avatar"></span><span class="uname">USER NAME</span></div>
  <div class="video" role="img" aria-label="Video post">
    <svg width="26" height="30" viewBox="0 0 34 38"><path d="M2 2 L32 19 L2 36 Z" fill="#ffffff"/></svg>
  </div>
  <div class="user"><span class="avatar"></span><span class="uname">USER NAME</span></div>
  <div class="video" role="img" aria-label="Video post">
    <svg width="26" height="30" viewBox="0 0 34 38"><path d="M2 2 L32 19 L2 36 Z" fill="#ffffff"/></svg>
  </div>
</section>

</body>
</html>
```